Varemo Group Business Card Design

The CEO is looking for a new trendy look for his business card.
You can stay with current branding or come up with something new/creative. It can be 3D, including Medical Office buildings. You can use our logo in a variety of colors. Please include name, title, company name, company website, email address, cell number

Target Market(s)

Real Estate Development and Construction

Industry/Entity Type

Health care real estate

Contact Information for Business Card

Rohesh Kumbar, CEO M-727.418.9062 E-roheshkumbar@varemo.com Address:4100 Lindell Ave, Tampa, FL 33611 www.varemo.com

Font styles to use
Other font styles liked:
• Be creative

Requirements
Must have
• Creative, trendy look
Nice to have
• Please go to our website to get a feel- www. varemo.com
Should not have
• small fonts

```html
<!DOCTYPE html>
<html lang="en">
<head>
<meta charset="utf-8">
<title>Varemo Group – Business Card</title>
<link rel="stylesheet" href="https://fonts.googleapis.com/css2?family=Arimo:wght@400;700&family=Open+Sans:wght@400&display=swap">
<style>
  :root{
    --bg:#e6e7e9;
    --navy:#0f1025;
    --red:#ec1c24;
    --white:#ffffff;
    --paper:#f3f3f3;
    --ink:#2a2a2e;
  }
  *{box-sizing:border-box;margin:0;padding:0}
  html,body{width:1200px;height:1200px;overflow:hidden;background:var(--bg)}
  .stage{position:relative;width:1200px;height:1200px}
  .card{position:absolute;left:294px;width:611px;border-radius:10px;overflow:hidden;
        box-shadow:4px 6px 8px rgba(0,0,0,.35)}
  .card--front{top:239px;height:348px;background:var(--navy)}
  .card--back{top:616px;height:350px;background:var(--paper)}
  .block{position:absolute}
  .red{background:var(--red)}
  .navy{background:var(--navy)}
  .white{background:var(--white)}
  .wordmark{position:absolute;font-family:"Arimo",sans-serif;font-weight:700;color:var(--white);white-space:nowrap}
  .front-wordmark{left:0;right:0;top:146px;text-align:center;font-size:46px;letter-spacing:-1px}
  .website{position:absolute;right:29px;bottom:18px;font-family:"Open Sans",sans-serif;font-size:23px;color:var(--white);letter-spacing:.3px}
  .logo-tile{position:absolute;left:63px;top:86px;width:165px;height:178px;border-radius:16px;background:var(--navy)}
  .tile-wordmark{left:0;right:0;top:74px;text-align:center;font-size:21px;letter-spacing:-.3px}
  .contact{position:absolute;left:318px;display:flex;align-items:flex-start;gap:9px;
           font-family:"Arimo",sans-serif;font-size:21px;color:var(--ink);line-height:27px;white-space:nowrap}
  .contact--email{font-size:19px}
  .icon{width:26px;height:22px;border-radius:3px;background:var(--red);display:flex;align-items:center;justify-content:center;flex:none;margin-top:3px}
  .name-panel{position:absolute;left:316px;top:134px;width:300px;height:82px;background:var(--navy);border-radius:7px 0 0 7px}
  .name{position:absolute;left:57px;top:14px;font-family:"Arimo",sans-serif;font-weight:700;font-size:23px;color:var(--white);letter-spacing:.2px;white-space:nowrap}
  .title{position:absolute;left:57px;top:42px;font-family:"Arimo",sans-serif;font-weight:700;font-size:23px;color:var(--red)}
  .person-icon{position:absolute;left:14px;top:26px}
</style>
</head>
<body>
<div class="stage">

  <section class="card card--front">
    <div class="block red" style="left:0;top:135px;width:22px;height:78px"></div>
    <div class="block red" style="left:530px;top:135px;width:81px;height:78px"></div>
    <div class="block white" style="left:589px;top:112px;width:22px;height:23px"></div>
    <div class="block white" style="left:589px;top:213px;width:22px;height:23px"></div>
    <div class="wordmark front-wordmark">Varemo Group</div>
    <div class="website">www.varemo.com</div>
  </section>

  <section class="card card--back">
    <div class="block navy" style="left:0;top:0;width:20px;height:350px"></div>
    <div class="block red" style="left:0;top:49px;width:20px;height:252px"></div>

    <div class="logo-tile"><div class="wordmark tile-wordmark">Varemo Group</div></div>

    <div class="contact" style="top:83px">
      <span class="icon"><svg width="14" height="14" viewBox="0 0 24 24"><path fill="#fff" d="M6.6 10.8a15.1 15.1 0 0 0 6.6 6.6l2.2-2.2a1 1 0 0 1 1-.25 11.4 11.4 0 0 0 3.6.57 1 1 0 0 1 1 1V20a1 1 0 0 1-1 1A17 17 0 0 1 3 4a1 1 0 0 1 1-1h3.5a1 1 0 0 1 1 1c0 1.25.2 2.45.57 3.57a1 1 0 0 1-.25 1z"/></svg></span>
      <span>727.418.9062</span>
    </div>

    <div class="block red" style="left:590px;top:122px;width:22px;height:12px"></div>
    <div class="block red" style="left:590px;top:216px;width:22px;height:12px"></div>
    <div class="name-panel">
      <svg class="person-icon" width="28" height="32" viewBox="0 0 28 32" fill="none" stroke="#fff" stroke-width="2">
        <circle cx="14" cy="8" r="6"/>
        <path d="M2 30v-5a8 8 0 0 1 8-8h8a8 8 0 0 1 8 8v5z"/>
        <path d="M11 18l3 5 3-5"/>
      </svg>
      <div class="name">ROHESH KUMBAR</div>
      <div class="title">CEO</div>
    </div>

    <div class="contact contact--email" style="top:238px">
      <span class="icon"><svg width="16" height="12" viewBox="0 0 16 12" fill="none" stroke="#fff" stroke-width="1.5"><rect x="1" y="1" width="14" height="10"/><path d="M1 1l7 6 7-6M1 11l5-5M15 11l-5-5"/></svg></span>
      <span>roheshkumbar@varemo.com</span>
    </div>

    <div class="contact" style="top:270px">
      <span class="icon" style="margin-top:17px"><svg width="14" height="13" viewBox="0 0 14 13"><path fill="#fff" d="M7 0l7 6h-2v7H9V9H5v4H2V6H0z"/></svg></span>
      <span>4100 Lindell Ave,<br>Tampa, FL 33611.</span>
    </div>
  </section>

</div>
</body>
</html>
```